Typing Service Business Card Design

Need a new business card design for new logo update. The Keyline Crew is an outsourced typing service. We type audio / voice files into word documents. We are a professional service that is recognised in the industry over the past 15 years and have a strong connection to our brand. The final design should be professional, simple, yet effective.

Business

Contact Information for Business Card

Rosalind Varga
Director

rosalind@kbq.com.au
www.thekeylinecrewbase.com.au

```html
<!DOCTYPE html>
<html lang="en">
<head>
<meta charset="utf-8">
<title>The Keyline Crew – Business Card</title>
<link rel="stylesheet" href="https://fonts.googleapis.com/css2?family=Open+Sans:wght@400;600&family=Roboto+Condensed:wght@300&display=swap">
<style>
  :root {
    --magenta: #c2448f;
    --ink: #050505;
    --paper: #ffffff;
    --backdrop: #ecebea;
    --text-dark: #1a0a14;
  }
  * { margin: 0; padding: 0; box-sizing: border-box; }
  html, body {
    width: 1200px;
    height: 902px;
    overflow: hidden;
    background: var(--backdrop);
    font-family: "Open Sans", Arial, sans-serif;
  }
  .sheet {
    width: 1200px;
    height: 902px;
    display: flex;
    flex-direction: column;
    align-items: center;
    justify-content: center;
    gap: 44px;
  }
  .card {
    position: relative;
    width: 700px;
    height: 389px;
    overflow: hidden;
    box-shadow: 0 6px 18px rgba(0,0,0,0.18);
  }

  /* Back side */
  .card--back {
    background: var(--magenta);
    display: flex;
    align-items: center;
    justify-content: center;
  }
  .card--back .brand-name {
    color: var(--paper);
    font-size: 58px;
    font-weight: 600;
    letter-spacing: -0.5px;
  }

  /* Front side */
  .card--front { background: var(--magenta); }
  .front__band {
    position: absolute;
    left: 0; top: 0;
    width: 100%;
    height: 212px;
    background: var(--ink);
    border-bottom: 4px solid var(--paper);
  }
  .front__brand {
    position: absolute;
    left: 0; right: 0;
    top: 74px;
    text-align: center;
  }
  .front__brand .brand-name {
    color: var(--magenta);
    font-size: 50px;
    font-weight: 600;
    letter-spacing: -0.5px;
    line-height: 1;
  }
  .front__tagline {
    margin-top: 16px;
    padding-left: 170px;
    color: var(--paper);
    font-family: "Roboto Condensed", "Arial Narrow", sans-serif;
    font-weight: 300;
    font-size: 34px;
    line-height: 1;
  }
  .front__person {
    position: absolute;
    left: 0; right: 0;
    top: 228px;
    text-align: center;
    padding-left: 60px;
  }
  .person__name {
    color: var(--paper);
    font-size: 30px;
    font-weight: 400;
    line-height: 1.15;
  }
  .person__role {
    color: var(--text-dark);
    font-size: 21px;
    line-height: 1.2;
  }
  .front__contact {
    position: absolute;
    left: 0; right: 0;
    top: 320px;
    text-align: center;
    padding-left: 60px;
    color: var(--text-dark);
    font-size: 21px;
    line-height: 1.25;
  }
</style>
</head>
<body>
  <main class="sheet">
    <section class="card card--back" aria-label="Business card back">
      <span class="brand-name">The Keyline Crew</span>
    </section>

    <section class="card card--front" aria-label="Business card front">
      <div class="front__band"></div>
      <div class="front__brand">
        <div class="brand-name">The Keyline Crew</div>
        <div class="front__tagline">You speak. We key.</div>
      </div>
      <div class="front__person">
        <div class="person__name">Rosalind Varga</div>
        <div class="person__role">Director</div>
      </div>
      <div class="front__contact">
        <div class="contact__email">rosalind@kbq.com.au</div>
        <div class="contact__web">www.thekeylinecrewbase.com.au</div>
      </div>
    </section>
  </main>
</body>
</html>
```